Business Card Design

Great brand name mattresses at bulk prices, quality affordable for everyone.

something relating to a mattress is important for the card please.

Industry/Entity Type

Business

Contact Information for Business Card

Tervo Mattress

Requirements
Must have
• something related to a mattress, its the only thing we sell… the logo is not mandatory but would like, i understand the logo does not have a mattress

```html
<!DOCTYPE html>
<html lang="en">
<head>
<meta charset="utf-8">
<title>Tervo Mattress – Business Card</title>
<link rel="stylesheet" href="https://fonts.googleapis.com/css2?family=Roboto+Slab:wght@300;400&family=Roboto:wght@400;500;700&family=Oswald:wght@600&display=swap">
<style>
  :root {
    --orange: #f47c00;
    --gold: #ffcb05;
    --lemon: #ffff1a;
    --white: #ffffff;
    --ink: #1d1d1d;
    --text: #2a2a2a;
    --backdrop: #e9e6e1;
  }
  * { box-sizing: border-box; margin: 0; padding: 0; }
  html, body { width: 1200px; height: 900px; overflow: hidden; }
  body { background: var(--backdrop); position: relative; font-family: "Roboto", Arial, sans-serif; }

  .card {
    position: absolute;
    left: 276px;
    width: 648px;
    height: 380px;
    background: var(--white);
    overflow: hidden;
    box-shadow: 0 4px 12px rgba(0,0,0,.18);
  }
  .card--front { top: 53px; }
  .card--back { top: 466px; }

  .brand-band {
    position: absolute;
    left: 0; top: 0;
    width: 100%;
    background: var(--orange);
    display: flex;
    align-items: center;
    justify-content: center;
  }
  .card--front .brand-band { height: 164px; }
  .card--back .brand-band { height: 166px; }

  .brand-name {
    font-family: "Roboto Slab", Georgia, serif;
    font-weight: 400;
    font-size: 54px;
    letter-spacing: 0.5px;
    color: var(--white);
    white-space: nowrap;
  }

  .product-ring { position: absolute; left: 0; top: 0; }

  .badge-brands {
    position: absolute;
    left: 379px; top: 172px;
    width: 160px; height: 160px;
    border-radius: 50%;
    background: var(--gold);
    display: flex; flex-direction: column; justify-content: center;
    padding-left: 22px;
    font-family: "Oswald", Impact, sans-serif;
    font-weight: 600;
    font-size: 28px;
    line-height: 1.02;
    letter-spacing: 5px;
    color: var(--white);
  }

  .badge-discount {
    position: absolute;
    left: 538px; top: 127px;
    width: 86px; height: 86px;
    border-radius: 50%;
    background: var(--lemon);
    border: 3px solid var(--white);
    display: flex; flex-direction: column; align-items: center; justify-content: center;
    color: var(--ink);
    text-align: center;
  }
  .badge-discount__value { font-weight: 700; font-size: 20px; line-height: 1; }
  .badge-discount__label { font-weight: 400; font-size: 32px; line-height: .95; }

  .team {
    position: absolute;
    right: 440px; top: 250px;
    text-align: right;
  }
  .person + .person { margin-top: 17px; }
  .person__name { color: var(--orange); font-weight: 500; font-size: 17px; line-height: 22px; }
  .person__role { color: var(--text); font-size: 15px; line-height: 20px; }

  .divider {
    position: absolute;
    left: 233px; top: 232px;
    width: 2px; height: 148px;
    background: var(--ink);
  }

  .contact { position: absolute; left: 250px; top: 236px; }
  .contact__row { display: flex; align-items: center; }
  .contact__row + .contact__row { margin-top: 4px; }
  .contact__icon { width: 36px; height: 36px; flex: none; margin-right: 8px; }
  .contact__lines {
    font-family: "Roboto Slab", Georgia, serif;
    font-weight: 300;
    font-size: 15px;
    line-height: 21px;
    color: var(--text);
  }
</style>
</head>
<body>

<section class="card card--front" aria-label="Business card front">
  <header class="brand-band">
    <span class="brand-name">TERVO MATTRESS</span>
  </header>

  <svg class="product-ring" width="648" height="380" viewBox="0 0 648 380" aria-hidden="false">
    <defs>
      <linearGradient id="mattressTone" x1="0" y1="0" x2="1" y2="1">
        <stop offset="0" stop-color="#e4e8ee"/>
        <stop offset="1" stop-color="#a9b2bf"/>
      </linearGradient>
      <clipPath id="ringClip"><circle cx="60" cy="282" r="160"/></clipPath>
    </defs>
    <circle cx="60" cy="282" r="163" fill="var(--white)" stroke="var(--lemon)" stroke-width="7"/>
    <g clip-path="url(#ringClip)">
      <rect x="0" y="180" width="210" height="200" rx="6" fill="url(#mattressTone)"
            role="img" aria-label="Photo of a stack of four white mattresses"/>
    </g>
  </svg>

  <div class="badge-brands"><span>Best</span><span>Brands</span></div>

  <div class="badge-discount">
    <span class="badge-discount__value">75%</span>
    <span class="badge-discount__label">Off</span>
  </div>
</section>

<section class="card card--back" aria-label="Business card back">
  <header class="brand-band">
    <span class="brand-name">TERVO MATTRESS</span>
  </header>

  <div class="team">
    <div class="person">
      <div class="person__name">Marco Alvarez</div>
      <div class="person__role">President</div>
    </div>
    <div class="person">
      <div class="person__name">Daniel Alvarez</div>
      <div class="person__role">Manager</div>
    </div>
  </div>

  <div class="divider"></div>

  <div class="contact">
    <div class="contact__row">
      <svg class="contact__icon" viewBox="0 0 36 36" aria-hidden="true">
        <path d="M18 5 L33 18 L29 18 L29 31 L21 31 L21 23 L15 23 L15 31 L7 31 L7 18 L3 18 Z" fill="var(--orange)"/>
      </svg>
      <div class="contact__lines">
        4120 SW, 92 Avenue, Unit 12, Tervo, FL 33100<br>
        57 NW, 140 Street, Tervo, FL 33102
      </div>
    </div>
    <div class="contact__row">
      <svg class="contact__icon" viewBox="0 0 36 36" aria-hidden="true">
        <circle cx="18" cy="18" r="14" fill="none" stroke="var(--orange)" stroke-width="2"/>
        <path d="M13 9 C11 11 11 16 14 21 C17 26 21 28 24 27 L25.5 24 L22 21.5 L20 23 C18 22 15.5 18.5 15 16 L17 14.5 L15.5 10.5 Z" fill="var(--orange)"/>
      </svg>
      <div class="contact__lines">
        (555) 210 4837<br>
        (555) 382 0916
      </div>
    </div>
    <div class="contact__row">
      <svg class="contact__icon" viewBox="0 0 36 36" aria-hidden="true">
        <g fill="none" stroke="var(--orange)" stroke-width="2">
          <circle cx="18" cy="18" r="14"/>
          <ellipse cx="18" cy="18" rx="6" ry="14"/>
          <line x1="4" y1="18" x2="32" y2="18"/>
          <path d="M6.5 11 H29.5 M6.5 25 H29.5"/>
        </g>
      </svg>
      <div class="contact__lines">
        info@tervomattress.com<br>
        www.tervomattress.com
      </div>
    </div>
  </div>
</section>

</body>
</html>
```